Business Cards Needed for Innovative Healthcare Marketing Company

We are a marketing company focused on healthcare. Our company is all about rebranding yourself renewing your image and generating results. The phoenix stands for "reborn" or "rising" which we provide new brands for our clients we take their old brands and renew it with creativity and innovation. I am looking for a business card with color dimension. I have attached an example of a card I think has the look and feel of what I am trying to accomplish. I like that the card example has black and grey font colors, I like the font placement and the small logo, I really like the use of the colors on the right those are the colors of my logo. My logo is phoenix so maybe incorporating flames similar to that design. I would like the back a solid color maybe red with an opaque version of the logo and website. As a marketing company I am always open to creative liberty!

Target Market(s)

Doctors and business professionals.

Industry/Entity Type

Marketing

Contact Information for Business Card

Vornaly Health Care Marketing
Marnie Okonski- CEO
#(502)638-2947
email-marnie@vornaly.com
website- vornaly.com

Font styles to use
Sans Serif

Colors
ec1f27
f37122
ffc214
fbed22
fbf289
f04a50

Requirements
Must have
• The logo and required information
Nice to have
• icons by the information
Should not have
• child like font

```html
<!DOCTYPE html>
<html lang="en">
<head>
<meta charset="utf-8">
<title>Vornaly Health Care Marketing – Business Card</title>
<link href="https://fonts.googleapis.com/css2?family=Arimo:ital@1&family=Francois+One&family=Open+Sans:wght@400;600&display=swap" rel="stylesheet">
<style>
  :root {
    --board: #ede8de;
    --crimson: #9b1c22;
    --red: #ec1f27;
    --orange: #f37122;
    --amber: #ffc214;
    --coral: #f04a50;
    --paper: #f7f5f1;
    --ink: #111111;
    --label: #222222;
    --white: #ffffff;
  }
  * { margin: 0; padding: 0; box-sizing: border-box; }
  html, body { width: 1200px; height: 1000px; overflow: hidden; }
  body { background: var(--board); position: relative; font-family: "Open Sans", Arial, sans-serif; }

  .side-label {
    position: absolute; left: 182px;
    font-family: "Arimo", Arial, sans-serif; font-style: italic;
    font-size: 21px; color: var(--label);
  }
  .side-label--front { top: 264px; }
  .side-label--back { top: 602px; }

  .card { position: absolute; overflow: hidden; }
  .card--front { left: 306px; top: 110px; width: 546px; height: 302px; background: var(--crimson); }
  .card--back { left: 306px; top: 463px; width: 551px; height: 305px; background: var(--paper); }

  .brand { position: absolute; display: flex; align-items: center; gap: 10px; }
  .brand__mark { width: 34px; height: 34px; border-radius: 50%; flex: none; }
  .brand__name { font-family: "Open Sans", Arial, sans-serif; font-weight: 400; line-height: 1.15; letter-spacing: 0.5px; }

  .card--front .brand { left: 137px; top: 118px; }
  .card--front .brand__mark { background: var(--white); }
  .card--front .brand__name { color: var(--white); font-size: 16px; width: 140px; }

  .card--back .brand { left: 82px; top: 72px; }
  .card--back .brand__mark { background: var(--orange); }
  .card--back .brand__name { color: var(--crimson); font-size: 16px; width: 140px; }

  .flame { position: absolute; }
  .flame--front {
    right: 0; bottom: 0; width: 250px; height: 138px;
    border-top-left-radius: 100% 100%;
    background: linear-gradient(160deg, var(--amber) 0%, var(--orange) 55%, var(--red) 100%);
  }
  .flame--back-main {
    right: 0; top: 0; width: 212px; height: 305px;
    border-top-left-radius: 60% 30%; border-bottom-left-radius: 40% 60%;
    background: linear-gradient(170deg, var(--amber) 0%, var(--orange) 50%, var(--coral) 80%, var(--red) 100%);
  }
  .flame--back-edge {
    left: 0; bottom: 0; width: 34px; height: 128px;
    border-top-right-radius: 100% 70%;
    background: linear-gradient(180deg, var(--amber) 0%, var(--orange) 60%, var(--red) 100%);
  }

  .holder {
    position: absolute; left: 86px; top: 138px;
    font-family: "Francois One", Impact, sans-serif; font-size: 22px;
    color: var(--ink); letter-spacing: 0.3px;
  }
  .contact { position: absolute; left: 85px; top: 176px; list-style: none; }
  .contact__item {
    display: flex; align-items: center; gap: 10px;
    height: 30px; font-size: 16px; color: var(--ink); letter-spacing: 0.8px;
  }
  .contact__icon {
    width: 15px; height: 15px; border-radius: 2px; background: var(--red);
    color: var(--white); font-size: 10px; font-weight: 600; letter-spacing: 0;
    display: flex; align-items: center; justify-content: center; flex: none;
  }

  .mini { position: absolute; top: 847px; transform-origin: 0 0; }
  .mini--front { left: 390px; transform: scale(0.355); }
  .mini--back { left: 588px; transform: scale(0.35); }
  .mini .card { position: relative; left: 0; top: 0; }
</style>
</head>
<body>

  <span class="side-label side-label--front">Front</span>
  <span class="side-label side-label--back">Back</span>

  <section class="card card--front" aria-label="Card front">
    <div class="brand">
      <span class="brand__mark"></span>
      <span class="brand__name">VORNALY HEALTH CARE MARKETING</span>
    </div>
    <div class="flame flame--front" role="img" aria-label="Illustrated phoenix flame feathers in yellow, orange and red"></div>
  </section>

  <section class="card card--back" aria-label="Card back">
    <div class="brand">
      <span class="brand__mark"></span>
      <span class="brand__name">VORNALY HEALTH CARE MARKETING</span>
    </div>
    <h1 class="holder">Marnie Okonski- CEO</h1>
    <ul class="contact">
      <li class="contact__item"><span class="contact__icon">T</span>#(502)638-2947</li>
      <li class="contact__item"><span class="contact__icon">E</span>marnie@vornaly.com</li>
      <li class="contact__item"><span class="contact__icon">W</span>www.vornaly.com</li>
    </ul>
    <div class="flame flame--back-main" role="img" aria-label="Illustrated phoenix flame feathers in yellow, orange and red"></div>
    <div class="flame flame--back-edge" role="img" aria-label="Small flame feather tips at the card edge"></div>
  </section>

  <div class="mini mini--front">
    <section class="card card--front" aria-label="Card front preview">
      <div class="brand">
        <span class="brand__mark"></span>
        <span class="brand__name">VORNALY HEALTH CARE MARKETING</span>
      </div>
      <div class="flame flame--front" role="img" aria-label="Illustrated phoenix flame feathers"></div>
    </section>
  </div>

  <div class="mini mini--back">
    <section class="card card--back" aria-label="Card back preview">
      <div class="brand">
        <span class="brand__mark"></span>
        <span class="brand__name">VORNALY HEALTH CARE MARKETING</span>
      </div>
      <p class="holder">Marnie Okonski- CEO</p>
      <ul class="contact">
        <li class="contact__item"><span class="contact__icon">T</span>#(502)638-2947</li>
        <li class="contact__item"><span class="contact__icon">E</span>marnie@vornaly.com</li>
        <li class="contact__item"><span class="contact__icon">W</span>www.vornaly.com</li>
      </ul>
      <div class="flame flame--back-main" role="img" aria-label="Illustrated phoenix flame feathers"></div>
      <div class="flame flame--back-edge" role="img" aria-label="Small flame feather tips"></div>
    </section>
  </div>

</body>
</html>
```